Crimson Thunder Dill Pickles needs your smart gourmet Design

Looking for a smart design for a dill pickle jar container. The text
Crimson Thunder Dill Pickles.
Boldly Brined & Crisp.

A crunchy reason to open the fridge door.

Target Market(s)

Foodies, farmers market types.

Font styles to use
Serif
Sans Serif

Colors

Designer to choose colors to be used in the design.

Requirements
Must have
• Attractive design to entice foodies to buy my Pickles. Not cluttered, easy to read.
Nice to have
• Pickles, garlic. Modern.
Should not have
• Clutter. No script text.

```html
<!DOCTYPE html>
<html lang="en">
<head>
<meta charset="utf-8">
<title>Crimson Thunder Dill Pickles – Jar Label</title>
<link rel="stylesheet" href="https://fonts.googleapis.com/css2?family=Anton&family=Oswald:wght@600&family=Hind:wght@400;700&display=swap">
<style>
  :root {
    --page: #ffffff;
    --label-orange: #cc3300;
    --label-red: #990000;
    --wave-line: #000000;
    --ink-light: #ffffff;
    --pickle-green: #4a6a22;
    --pickle-dark: #33501a;
  }
  html, body {
    margin: 0;
    padding: 0;
    width: 1200px;
    height: 834px;
    overflow: hidden;
    background: var(--page);
  }
  .label {
    display: block;
    width: 1200px;
    height: 834px;
  }
  .label__top { fill: var(--label-orange); }
  .label__wave { fill: var(--label-red); }
  .label__wave-edge { fill: none; stroke: var(--wave-line); stroke-width: 3; }
  .brand-name {
    font-family: "Anton", "Oswald", sans-serif;
    fill: var(--ink-light);
  }
  .brand-name--first { font-size: 166px; }
  .brand-name--second { font-size: 198px; }
  .product-type {
    font-family: "Oswald", sans-serif;
    font-weight: 600;
    fill: var(--ink-light);
    font-size: 70px;
  }
  .slogan {
    font-family: "Hind", sans-serif;
    font-weight: 400;
    fill: var(--ink-light);
    font-size: 46px;
  }
  .tagline {
    font-family: "Hind", sans-serif;
    font-weight: 700;
    fill: var(--ink-light);
    font-size: 24px;
  }
</style>
</head>
<body>
<svg class="label" viewBox="0 0 1200 834" xmlns="http://www.w3.org/2000/svg">
  <defs>
    <linearGradient id="pickle-tone" x1="0" y1="0" x2="0" y2="1">
      <stop offset="0" stop-color="var(--pickle-green)"/>
      <stop offset="1" stop-color="var(--pickle-dark)"/>
    </linearGradient>
  </defs>

  <rect class="label__top" x="100" y="104" width="999" height="624"/>

  <path class="label__wave"
        d="M100 441 C130 458 180 462 240 474 C300 486 360 510 420 528 C470 543 520 556 560 572 C600 588 640 574 720 566 C790 560 830 530 880 520 C960 505 1040 530 1099 568 L1099 728 L100 728 Z"/>
  <path class="label__wave-edge"
        d="M100 441 C130 458 180 462 240 474 C300 486 360 510 420 528 C470 543 520 556 560 572 C600 588 640 574 720 566 C790 560 830 530 880 520 C960 505 1040 530 1099 568"/>

  <text class="brand-name brand-name--first" x="430" y="287" textLength="340" lengthAdjust="spacingAndGlyphs">CRIMSON</text>
  <text class="brand-name brand-name--second" x="430" y="477" textLength="340" lengthAdjust="spacingAndGlyphs">THUNDER</text>
  <text class="product-type" x="429" y="553" textLength="341" lengthAdjust="spacingAndGlyphs">DILL PICKLES</text>

  <rect class="mascot" x="877" y="348" width="167" height="247" rx="70"
        fill="url(#pickle-tone)" role="img"
        aria-label="Illustration of two cartoon pickle characters"/>

  <text class="slogan" x="359" y="647" textLength="481" lengthAdjust="spacingAndGlyphs">Boldly Brined &amp; Crisp</text>
  <text class="tagline" x="359" y="692" textLength="481" lengthAdjust="spacingAndGlyphs">A crunchy reason to open the fridge door.</text>
</svg>
</body>
</html>
```